International Heavy Earthmoving Freight forwarder needs a flyer design

We need a flyer design to send out on Linkedin, Facebook, e-mail blasts, instagram etc.
We would like to announce that we have just secured a new contract offering exceptionally low shipping rates from East Coast and Gulf USA to Indonesia, Malaysia, Thailand amongst other South East Asian countries.
I would like to make it an announcement like "Hot off the press"
You can visit our instagram page for photos @haulvane
I would like the contact person on the flyer to be:
Dean Harlow
dean.harlow@haulvane.example
+1 555 014 2286
www.haulvane.example

Target Market(s)

Import and export used machinery equioment dealers. Mining companies, earthmoving contractors, freight forwarders

Font styles to use
Sans Serif

Requirements
Must have
• Logo, contact details, some photos from various Haulvane media outlets

```html
<!DOCTYPE html>
<html lang="en">
<head>
<meta charset="utf-8">
<title>Haulvane – Hot Off The Press</title>
<link rel="stylesheet" href="https://fonts.googleapis.com/css2?family=Bebas+Neue&family=Open+Sans:wght@600&display=swap">
<style>
  :root {
    --red-deep: #8a0a14;
    --red: #c8161e;
    --red-bright: #e0202a;
    --gold-line: #d6a64a;
    --white: #ffffff;
    --ink: #1c1c1c;
    --panel-light: #f1f1f1;
    --panel-dark: #d4d4d4;
    --hazard-yellow: #f5c211;
    --hazard-black: #141414;
    --photo-sky: #c9d2d9;
    --photo-yellow: #c99a1e;
    --photo-dark: #3b3226;
    --corner-grey: #e4e4e4;
  }
  * { margin: 0; padding: 0; box-sizing: border-box; }
  html, body { width: 1043px; height: 1200px; overflow: hidden; background: #ffffff; }
  .flyer { position: relative; width: 1043px; height: 1200px; overflow: hidden; background: var(--red); }
  .hero-photo {
    position: absolute; left: 0; top: 0; width: 1043px; height: 600px;
    background: linear-gradient(150deg, var(--photo-sky) 0%, var(--photo-yellow) 35%, #a67c14 60%, var(--photo-dark) 100%);
  }
  .shapes { position: absolute; left: 0; top: 0; }
  .brand {
    position: absolute; left: 46px; top: 150px;
    display: flex; align-items: center; gap: 10px;
    font-family: "Open Sans", sans-serif; font-weight: 600; font-size: 26px;
    color: var(--ink); letter-spacing: 1px;
  }
  .brand-dot { width: 18px; height: 18px; background: var(--red-bright); }
  .map-glow {
    position: absolute; left: 60px; top: 660px; width: 920px; height: 400px;
    background: radial-gradient(ellipse at center, rgba(255,255,255,0.12), rgba(255,255,255,0) 70%);
  }
  .headline {
    position: absolute; left: 0; right: 0; top: 620px; text-align: center;
    font-family: "Bebas Neue", sans-serif; font-size: 100px; line-height: 1;
    color: var(--white); text-shadow: 2px 3px 4px rgba(0,0,0,0.35);
  }
  .divider {
    position: absolute; left: 98px; width: 847px; top: 766px; height: 1px;
    background: linear-gradient(90deg, rgba(214,166,74,0), var(--gold-line), rgba(214,166,74,0));
  }
  .announcement {
    position: absolute; left: 0; right: 0; top: 814px; text-align: center;
    font-family: "Bebas Neue", sans-serif; font-size: 44px; line-height: 63px;
    color: var(--white);
  }
  .contact {
    position: absolute; left: 0; top: 1050px; width: 1043px; height: 82px;
    background: linear-gradient(180deg, var(--panel-light), var(--panel-dark));
    font-family: "Open Sans", sans-serif; font-weight: 600; font-size: 28px;
    color: var(--ink); text-align: center; line-height: 40px; padding-top: 2px;
  }
  .contact-row { display: flex; justify-content: center; align-items: center; gap: 12px; }
  .phone-icon { width: 24px; height: 24px; margin-left: 14px; margin-right: -6px; }
  .footer-bar { position: absolute; left: 0; top: 1132px; width: 1043px; height: 68px; background: var(--red-bright); }
</style>
</head>
<body>
  <main class="flyer">
    <div class="hero-photo" role="img" aria-label="Photo of a large yellow mining haul truck being lifted, with a worker in a white hard hat and orange hi-vis vest watching"></div>

    <svg class="shapes" width="1043" height="1200" viewBox="0 0 1043 1200" aria-hidden="true">
      <defs>
        <linearGradient id="red-fade" x1="0" y1="0" x2="0" y2="1">
          <stop offset="0" stop-color="var(--red-deep)"/>
          <stop offset="0.45" stop-color="var(--red)"/>
          <stop offset="1" stop-color="var(--red-bright)"/>
        </linearGradient>
        <pattern id="hazard" width="60" height="40" patternUnits="userSpaceOnUse" patternTransform="skewX(-35)">
          <rect width="60" height="40" fill="var(--hazard-black)"/>
          <rect width="30" height="40" fill="var(--hazard-yellow)"/>
        </pattern>
        <linearGradient id="corner-fade" x1="0" y1="0" x2="1" y2="1">
          <stop offset="0" stop-color="#ffffff" stop-opacity="0.95"/>
          <stop offset="1" stop-color="var(--corner-grey)" stop-opacity="0.9"/>
        </linearGradient>
      </defs>
      <polygon points="0,0 647,0 0,273" fill="url(#corner-fade)"/>
      <polygon points="0,545 1043,453 1043,1200 0,1200" fill="url(#red-fade)"/>
      <polygon points="0,456 1043,513 1043,540 0,484" fill="url(#hazard)"/>
    </svg>

    <div class="brand"><span class="brand-dot"></span>HAULVANE</div>

    <div class="map-glow" role="img" aria-label="Faint world map in the background"></div>

    <h1 class="headline">HOT OFF THE PRESS</h1>
    <div class="divider"></div>
    <p class="announcement">
      New contract offering exceptionally low shipping rates<br>
      from East Coast and Gulf USA to Indonesia, Malaysia,<br>
      Thailand amongst other South East Asian countries
    </p>

    <section class="contact">
      <div class="contact-row">
        <span>Dean Harlow</span>
        <svg class="phone-icon" viewBox="0 0 24 24" aria-hidden="true">
          <path d="M6.6 10.8a15.1 15.1 0 0 0 6.6 6.6l2.2-2.2a1 1 0 0 1 1-.25 11.4 11.4 0 0 0 3.6.57 1 1 0 0 1 1 1V20a1 1 0 0 1-1 1A17 17 0 0 1 3 4a1 1 0 0 1 1-1h3.5a1 1 0 0 1 1 1c0 1.25.2 2.45.57 3.57a1 1 0 0 1-.25 1z" fill="var(--red-bright)"/>
        </svg>
        <span>+1 555 014 2286</span>
      </div>
      <div class="contact-row">
        <span>dean.harlow@haulvane.example</span><span>|</span><span>www.haulvane.example</span>
      </div>
    </section>
    <div class="footer-bar"></div>
  </main>
</body>
</html>
```